New Business Card Design Project

I need a clean, professional business card. I'd like it to have some color, but not be wild. We do technology consulting and we have clients large and small who trust us with some of their most important data and projects. Simple but not boring should drive all design proposals. Multicolored and two sided, but with a matte finish, I think.
For more on tone, check out our website: http://quorvantis.example

Target Market(s)

Upper management of respected businesses. Tech savvy, but not "hipster".

Industry/Entity Type

Business

Requirements
Must have
• Files need to be provided in .eps and in .pdf in a manner that allows for easy updates.
Must have Name, Title, Phone, Email, Twitter, Website
Nice to have
• Logo/Name shouldn't be too big. One thing I've read several places is that the bigger the logo, the smaller the brand. A good article on dos and don'ts here: http://www.brindlepost.example/2011/02/business-card-experience.html

```html
<!DOCTYPE html>
<html lang="en">
<head>
<meta charset="utf-8">
<title>Quorvantis Business Card</title>
<link rel="stylesheet" href="https://fonts.googleapis.com/css2?family=Arimo:ital,wght@0,400;0,700;1,400;1,700&family=Questrial&display=swap">
<style>
  :root {
    --stage: #5b3b25;
    --label: #1e140c;
    --card-white: #ffffff;
    --brand-green: #8aad3f;
    --brand-teal: #3e93a5;
    --brand-grey: #7d7f82;
    --ink: #3a3a3a;
    --ink-soft: #555555;
    --dot-tint: #eef2f5;
  }
  * { box-sizing: border-box; margin: 0; padding: 0; }
  html, body { width: 1200px; height: 788px; overflow: hidden; }
  body {
    background: var(--stage);
    position: relative;
    font-family: "Arimo", Arial, sans-serif;
  }
  .side-label {
    position: absolute;
    width: 525px;
    text-align: center;
    font-family: "Arimo", Arial, sans-serif;
    font-size: 22px;
    color: var(--label);
  }
  .card {
    position: absolute;
    width: 525px;
    height: 300px;
    border-radius: 18px;
    overflow: hidden;
    box-shadow: 0 4px 10px rgba(0,0,0,0.35);
  }
  .card--front, .card--back-white { background: var(--card-white); }
  .card--back-green { background: var(--brand-green); }
  .card--back-teal { background: var(--brand-teal); }

  .brand {
    position: absolute;
    display: flex;
    align-items: center;
    gap: 12px;
    font-family: "Questrial", Arial, sans-serif;
    font-size: 33px;
    letter-spacing: 1px;
    white-space: nowrap;
    line-height: 1;
  }
  .brand--centred {
    left: 0; right: 0;
    justify-content: center;
    font-size: 37px;
    transform: translateY(-50%);
  }
  .brand__dot {
    width: 14px; height: 14px; border-radius: 50%;
    background: var(--brand-teal);
    flex: none;
  }
  .brand--grey { color: var(--brand-grey); }
  .brand--white { color: #ffffff; }
  .brand--white .brand__dot { background: #ffffff; }
  .card--back-teal .brand__dot { background: var(--brand-green); }

  .front-texture {
    position: absolute;
    right: 0; top: 0;
    width: 200px; height: 175px;
    background: radial-gradient(ellipse at 80% 20%, #f1f1f1 0%, #fafafa 55%, rgba(255,255,255,0) 80%);
  }
  .back-texture {
    position: absolute;
    right: 0; top: 40px;
    width: 360px; height: 220px;
    background: radial-gradient(ellipse at 70% 50%, var(--dot-tint) 0%, #f6f8fa 50%, rgba(255,255,255,0) 78%);
  }

  .holder { position: absolute; left: 29px; top: 190px; }
  .holder__name { font-size: 17px; font-weight: 700; color: var(--brand-green); }
  .holder__title { font-size: 13px; font-weight: 700; color: var(--ink); margin-top: 3px; }
  .holder__phone { font-size: 13px; color: var(--ink-soft); margin-top: 17px; }

  .contact { position: absolute; left: 305px; top: 194px; font-size: 13px; color: var(--ink-soft); line-height: 21px; }
  .contact__key { font-style: italic; font-weight: 700; color: var(--ink); }

  .web-line {
    position: absolute;
    left: 0; right: 0;
    text-align: center;
    font-family: "Questrial", Arial, sans-serif;
    font-size: 19px;
    letter-spacing: 2px;
  }
  .web-line--dark { color: #3b3b3b; }
  .web-line--light { color: #ffffff; }
</style>
</head>
<body>

  <div class="side-label" style="left:56px; top:33px;">Front</div>
  <div class="side-label" style="left:622px; top:33px;">Back - 1</div>
  <div class="side-label" style="left:53px; top:404px;">Back - 2</div>
  <div class="side-label" style="left:624px; top:404px;">Back - 3</div>

  <section class="card card--front" style="left:56px; top:73px;">
    <div class="front-texture" role="img" aria-label="Soft embossed dot texture in the top right corner"></div>
    <div class="brand brand--grey" style="left:29px; top:52px;">
      <span class="brand__dot"></span>QUORVANTIS
    </div>
    <div class="holder">
      <p class="holder__name">Your Name</p>
      <p class="holder__title">Designation</p>
      <p class="holder__phone"><span class="contact__key">phone</span> : +12 555 01234</p>
    </div>
    <div class="contact">
      <p><span class="contact__key">twitter</span> : @quorvantislabs</p>
      <p><span class="contact__key">email</span> : info@quorvantis.example</p>
      <p><span class="contact__key">web</span> : www.quorvantis.example</p>
    </div>
  </section>

  <section class="card card--back-white" style="left:622px; top:73px;">
    <div class="back-texture" role="img" aria-label="Faint pale blue dot texture across the right side"></div>
    <div class="brand brand--grey brand--centred" style="top:105px;">
      <span class="brand__dot"></span>QUORVANTIS
    </div>
    <p class="web-line web-line--dark" style="top:259px;">www.quorvantis.example</p>
  </section>

  <section class="card card--back-green" style="left:53px; top:445px;">
    <div class="brand brand--white brand--centred" style="top:153px;">
      <span class="brand__dot"></span>QUORVANTIS
    </div>
    <p class="web-line web-line--light" style="top:245px;">www.quorvantis.example</p>
  </section>

  <section class="card card--back-teal" style="left:624px; top:445px;">
    <div class="brand brand--white brand--centred" style="top:147px;">
      <span class="brand__dot"></span>QUORVANTIS
    </div>
    <p class="web-line web-line--light" style="top:245px;">www.quorvantis.example</p>
  </section>

</body>
</html>
```